Motor Insurance Quotation - New Quote format / New Template

We are a 40 year old insurance company called 'Velmor Insurance Agency L.L.C' in Dubai, UAE (Our logo / color design can and details can be found on www.velmorgulf-example.com).

Velmor provides all kinds of insurance solutions for its clients...currently is this modern fast paced world of ever changing technology and increasing competition we need to be ahead of our competitors...

In order to do so, we are in need to re-design our motor insurance quotation format / template and require it to be more attractive, modern and professional.
Since it is a text heavy format, we need it to look aesthetically appealing to our clients.

We would like to see designs that use our color code (as our website / sample quote currently used is attached)..these designs are required in pdf illustrator formats....i have also attached quotation formats used in the existing market. the template and the samples are only for reference and the templates are not to be followed.

Target Market(s)

UAE

Industry/Entity Type

Insurance

Font styles to use
Other font styles liked:
• arial

Requirements
Must have
• Aesthetic Design, Insurance details and covers provided in our quote, Velmor logo, color code (details can be found on our website)
Nice to have
• 1 page (short quote) and 2 page (detailed quote) designs to shared...

```html
<!DOCTYPE html>
<html lang="en">
<head>
<meta charset="utf-8">
<title>Velmor Motor Insurance Quotation</title>
<link href="https://fonts.googleapis.com/css2?family=Arimo:wght@400;700&display=swap" rel="stylesheet">
<style>
:root{
  --purple:#8b2a8f;
  --navy:#1d2a8a;
  --pink:#efd9ee;
  --grey:#e2e6ee;
  --paper:#ffffff;
  --ink:#1d2a8a;
  --stage:#2d2d30;
  --footer-bg:#eef0f5;
}
*{margin:0;padding:0;box-sizing:border-box}
html,body{width:1200px;height:776px;overflow:hidden;background:var(--stage);font-family:"Arimo",Arial,sans-serif}
.page{position:absolute;top:20px;width:520px;height:736px;background:var(--paper);overflow:hidden}
.page--quote{left:56px}
.page--card{left:624px}
.page-header{position:absolute;left:0;top:0;width:520px;height:60px}
.brand{position:absolute;left:26px;top:22px;font-size:26px;font-weight:400;color:var(--navy);letter-spacing:1px}
.doc-title{position:absolute;left:0;top:62px;width:520px;height:14px;background:var(--grey);font-size:6px;font-weight:700;color:var(--navy);padding:4px 0 0 18px}
.doc-title::after{content:"";position:absolute;right:0;top:0;width:130px;height:14px;background:var(--navy);clip-path:polygon(10% 0,100% 0,100% 100%,0 100%)}
.page--card .doc-title{top:90px;width:150px}
.page--card .doc-title::after{width:14px;right:-2px;clip-path:polygon(70% 0,100% 0,30% 100%,0 100%)}

.quote-body{position:absolute;left:34px;top:82px;width:452px}
.sec{height:10px;background:var(--purple);color:#fff;font-size:6px;font-weight:700;text-align:center;line-height:10px;clip-path:polygon(3% 0,100% 0,97% 100%,0 100%);margin-top:2px}
.sec--split{display:grid;grid-template-columns:24% 20% 36% 20%}
.sec--split span:nth-child(2),.sec--split span:nth-child(4){background:var(--navy)}
.row{display:grid;grid-template-columns:40% 60%;height:9.5px;font-size:5.8px;color:var(--ink);line-height:9.5px;text-align:center;white-space:nowrap;overflow:hidden}
.row:nth-child(odd){background:var(--pink)}
.row:nth-child(even){background:var(--grey)}
.row span:first-child{font-weight:700;border-right:1px solid #fff}
.row--single{grid-template-columns:100%}
.row--single span:first-child{border:0}
.cover-head{display:grid;grid-template-columns:38% 30% 32%;height:10px;font-size:6px;font-weight:700;color:#fff;line-height:10px;text-align:center;margin-top:2px}
.cover-head span:nth-child(1){background:var(--purple);clip-path:polygon(4% 0,100% 0,100% 100%,0 100%)}
.cover-head span:nth-child(2){background:var(--navy)}
.cover-head span:nth-child(3){background:var(--purple);clip-path:polygon(0 0,100% 0,96% 100%,0 100%)}
.cover .row{grid-template-columns:38% 30% 32%;font-size:5.4px}
.cover .row span:nth-child(2){border-right:1px solid #fff}
.note{font-size:5.6px;color:#fff;text-align:center;line-height:7px;padding:2px 20px;clip-path:polygon(3% 0,100% 0,97% 100%,0 100%);margin-top:2px;background:var(--purple)}
.note--navy{background:var(--navy)}
.note u{display:block}
.docs{display:grid;grid-template-columns:repeat(3,1fr);gap:2px;margin-top:2px}
.docs ul{list-style:none}
.docs li{height:10px;font-size:5.6px;font-weight:700;color:var(--ink);text-align:center;line-height:10px;background:var(--grey);white-space:nowrap}
.docs li:nth-child(even){background:var(--pink)}
.docs li.tab{background:var(--purple);color:#fff;clip-path:polygon(5% 0,100% 0,95% 100%,0 100%)}
.docs li.tab--navy{background:var(--navy)}
.docs li.blank{background:transparent}

.page-footer{position:absolute;left:0;bottom:0;width:520px;height:120px}
.footer-art{position:absolute;left:0;top:0}
.office{position:absolute;left:34px;top:40px;color:var(--navy);font-size:6.5px;font-weight:700;line-height:8px;font-style:normal}
.office h3{font-size:11px;color:var(--purple);font-weight:700;line-height:13px}
.office .ic{display:inline-block;width:5px;height:5px;margin-right:3px;vertical-align:middle}
.office .pair span{margin-right:12px}
.legal{position:absolute;right:40px;top:0;width:140px;font-size:4.6px;color:#8890b0;line-height:5.4px}

/* credit card page */
.label{position:absolute;left:60px;width:120px;height:10px;background:var(--purple);color:#fff;font-size:5.6px;font-weight:700;text-align:center;line-height:10px;clip-path:polygon(6% 0,100% 0,94% 100%,0 100%)}
.input{position:absolute;left:178px;width:300px;height:9px;background:var(--grey)}
.input--pink{background:var(--pink)}
.box{position:absolute;width:12px;height:9px;background:var(--grey)}
.box--pink{background:var(--pink)}
.hint{position:absolute;font-size:5px;line-height:9px;color:var(--navy);font-weight:700}
.band{position:absolute;left:60px;width:420px;height:12px;background:var(--purple);color:#fff;font-size:5.6px;text-align:center;line-height:12px;clip-path:polygon(2% 0,100% 0,98% 100%,0 100%)}
.band--notice{height:18px;line-height:7px;padding-top:2px}
.panel{position:absolute;left:70px;width:400px;background:var(--grey)}
.aed{position:absolute;left:70px;width:400px;height:12px;background:var(--grey);font-size:6px;color:var(--navy);padding:3px 4px}
</style>
</head>
<body>

<section class="page page--quote">
  <header class="page-header">
    <svg class="header-art" width="520" height="60" viewBox="0 0 520 60">
      <polygon points="240,10 520,10 520,24 300,24 288,36 230,36" fill="#e2e6ee"/>
      <polygon points="300,26 520,26 520,31 296,31" fill="#8b2a8f"/>
      <polygon points="186,10 212,10 178,42 152,42" fill="#8b2a8f"/>
      <polygon points="218,10 238,10 204,42 184,42" fill="#1d2a8a"/>
      <polygon points="244,10 256,10 222,42 210,42" fill="#8b2a8f"/>
    </svg>
    <div class="brand">VELMOR</div>
  </header>
  <div class="doc-title">MOTOR COMPREHENSIVE, FIRE, THEFT &amp; THIRD PARTY LIABILITY</div>

  <div class="quote-body">
    <div class="sec sec--split"><span>Quote Reference</span><span>MVA/2016/00603OM</span><span>Date of Issue</span><span>12/01/2017</span></div>

    <div class="sec">Driver Details</div>
    <div class="rows">
      <div class="row"><span>Insured Name</span><span>Layla Haddad</span></div>
      <div class="row"><span>Address</span><span>Dubai</span></div>
      <div class="row"><span>Phone Number</span><span>050 0000000</span></div>
      <div class="row"><span>Email</span><span>layla.h@mail-example.com</span></div>
      <div class="row"><span>Age</span><span>26 Years</span></div>
    </div>

    <div class="sec">Vehicle Details</div>
    <div class="rows">
      <div class="row"><span>Make</span><span>Orvant</span></div>
      <div class="row"><span>Model</span><span>S3</span></div>
      <div class="row"><span>Year of Make</span><span>2011</span></div>
      <div class="row"><span>Seating Capacity</span><span>5</span></div>
      <div class="row"><span>Body</span><span>Saloon</span></div>
    </div>

    <div class="sec">Type of Cover</div>
    <div class="rows">
      <div class="row row--single"><span>Comprehensive, Fire, Theft &amp; Third Party Liability</span></div>
    </div>

    <div class="sec">Quote Details</div>
    <div class="rows">
      <div class="row"><span>Sum Insured</span><span>AED 40,000.00</span></div>
      <div class="row"><span>Premium</span><span>AED 1,740.00</span></div>
      <div class="row"><span>Excess</span><span>AED 350.00</span></div>
    </div>

    <div class="cover-head"><span>Cover</span><span>Coverage / Cost</span><span>Limit</span></div>
    <div class="cover">
      <div class="row"><span>Personal Accident Benefits for Driver</span><span>Included</span><span>AED 200,000</span></div>
      <div class="row"><span>Personal Accident Benefits for Passengers</span><span>Included</span><span>AED 200,000 per Passenger</span></div>
      <div class="row"><span>RoadCare Roadside Assistance - Silver Card</span><span>Included</span><span>Unlimited (Once every 24 hours)</span></div>
      <div class="row"><span>RoadCare Roadside Assistance - Gold Card</span><span>Optional / AED 100</span><span>Registration Service &amp; Off Road Pull Out</span></div>
      <div class="row"><span>Rent a Car Option</span><span>Optional / AED 280</span><span>3 times per year, 10 days each</span></div>
      <div class="row"><span>Agency Repairs</span><span>Excluded</span><span>Excess AED 750</span></div>
      <div class="row"><span>Off Road Cover</span><span>Excluded</span><span>-</span></div>
      <div class="row"><span>Orange Card</span><span>Optional / Tariff Attached</span><span>-</span></div>
      <div class="row"><span>Territorial Limits</span><span>Included</span><span>UAE</span></div>
      <div class="row"><span>Third Party Bodily Injury</span><span>Included</span><span>Unlimited</span></div>
      <div class="row"><span>Third Party Property Damage</span><span>Included</span><span>AED 5,000,000</span></div>
      <div class="row"><span>Ambulance Cover</span><span>Included</span><span>-</span></div>
      <div class="row"><span>Windscreen Claims</span><span>Included</span><span>Excess will apply</span></div>
      <div class="row"><span>Medical Expenses</span><span>Included</span><span>AED 10,000 / Person</span></div>
      <div class="row"><span>Personal Effects (Theft subject to forcible entry)</span><span>Included</span><span>AED 4,000</span></div>
      <div class="row"><span>Natural Calamities</span><span>Included</span><span>-</span></div>
    </div>

    <p class="note">Where the insured requests the replacement of the damaged parts with new parts, the insured shall bear the rates of depreciation i.e. nil for brand new vehicles, 5% for the 2nd year, 10% for the 3rd year, 15% for the 4th year, 20% for the 5th year and a maximum of 30% for the 6th year onwards.</p>
    <p class="note note--navy">An Excess of 10% (besides the normal excess) of the amount of the accident is applicable for drivers who are less than 25 years of age <u>This insurance is non transferrable</u></p>
    <div class="sec">Should you accept the above terms, kindly provide us with the following:</div>

    <div class="docs">
      <ul>
        <li class="blank"></li>
        <li class="tab">New Client</li>
        <li>Passport &amp; Visa Copy</li>
        <li>Driving License copy</li>
        <li>Registration Card / Purchase Agreement Copy</li>
      </ul>
      <ul>
        <li class="blank"></li>
        <li>Financing Bank name, if any</li>
        <li>Mobile Number &amp; P.O. Box Number</li>
        <li>Attached Credit Form Copy</li>
      </ul>
      <ul>
        <li class="tab tab--navy">Existing Client</li>
        <li>Registration Card / Purchase Agreement Copy</li>
        <li>Financing Bank name, if any</li>
        <li>Attached Credit Form Copy</li>
      </ul>
    </div>
  </div>

  <footer class="page-footer">
    <svg class="footer-art" width="520" height="120" viewBox="0 0 520 120">
      <rect x="0" y="30" width="520" height="90" fill="#eef0f5"/>
      <polygon points="0,30 520,24 520,29 0,35" fill="#8b2a8f"/>
      <polygon points="330,88 520,88 520,96 322,96" fill="#8b2a8f"/>
      <polygon points="300,100 520,100 520,112 290,112" fill="#8b2a8f"/>
    </svg>
    <div class="legal">Registered name: Velmor Insurance Agency LLC<br>General Agents for Al Sahel National Insurance Co. (PSC)<br>Insurance Agents Registration No. 18<br>A member of the Velmor Insurance Group</div>
    <address class="office">
      <h3>Velmor Dubai</h3>
      Al Noor Street, Crescent Business Bldg.<br>
      <svg class="ic" viewBox="0 0 10 10"><path d="M5 0a4 4 0 0 1 4 4c0 3-4 6-4 6S1 7 1 4a4 4 0 0 1 4-4z" fill="#8b2a8f"/></svg>P.O.Box 4821, Dubai, UAE<br>
      <span class="pair"><span><svg class="ic" viewBox="0 0 10 10"><path d="M2 0l2 3-1 1c1 2 2 3 4 4l1-1 2 2-2 1C4 10 0 6 0 2z" fill="#8b2a8f"/></svg>+971 4 000 1234</span><span><svg class="ic" viewBox="0 0 10 10"><rect x="1" y="2" width="8" height="6" fill="#8b2a8f"/></svg>+971 4 000 5678</span></span><br>
      <span class="pair"><span><svg class="ic" viewBox="0 0 10 10"><circle cx="5" cy="5" r="4" fill="#8b2a8f"/></svg>www.velmorgulf-example.com</span><span><svg class="ic" viewBox="0 0 10 10"><rect x="0" y="2" width="10" height="6" fill="#8b2a8f"/></svg>info@velmorgulf-example.com</span></span>
    </address>
  </footer>
</section>

<section class="page page--card">
  <header class="page-header">
    <svg class="header-art" width="520" height="60" viewBox="0 0 520 60">
      <polygon points="240,10 520,10 520,24 300,24 288,36 230,36" fill="#e2e6ee"/>
      <polygon points="300,26 520,26 520,31 296,31" fill="#8b2a8f"/>
      <polygon points="186,10 212,10 178,42 152,42" fill="#8b2a8f"/>
      <polygon points="218,10 238,10 204,42 184,42" fill="#1d2a8a"/>
      <polygon points="244,10 256,10 222,42 210,42" fill="#8b2a8f"/>
    </svg>
    <div class="brand">VELMOR</div>
  </header>
  <div class="doc-title">CREDIT CARD AUTHORISATION</div>

  <div class="input" style="top:110px"></div>
  <div class="label" style="top:124px">Name of the Insured</div><div class="input input--pink" style="top:124px"></div>
  <div class="label" style="top:138px">Policy / Invoice Number</div><div class="input" style="top:138px"></div>
  <div class="label" style="top:152px">Mobile / Telephone No</div><div class="input input--pink" style="top:152px"></div>
  <div class="label" style="top:166px">(Mandatory) Email ID</div><div class="input" style="top:166px"></div>

  <div class="label" style="top:196px">NOVA CARD</div><div class="box" style="top:196px;left:184px"></div>
  <div class="label" style="top:210px">PRIME CARD</div><div class="box box--pink" style="top:210px;left:184px"></div>

  <div class="label" style="top:236px">Credit Card number</div>
  <div class="box" style="top:236px;left:184px"></div><div class="box" style="top:236px;left:198px"></div><div class="box" style="top:236px;left:212px"></div><div class="box" style="top:236px;left:226px"></div>
  <div class="box" style="top:236px;left:246px"></div><div class="box" style="top:236px;left:260px"></div><div class="box" style="top:236px;left:274px"></div><div class="box" style="top:236px;left:288px"></div>
  <div class="box" style="top:236px;left:308px"></div><div class="box" style="top:236px;left:322px"></div><div class="box" style="top:236px;left:336px"></div><div class="box" style="top:236px;left:350px"></div>
  <div class="box" style="top:236px;left:370px"></div><div class="box" style="top:236px;left:384px"></div><div class="box" style="top:236px;left:398px"></div><div class="box" style="top:236px;left:412px"></div>

  <div class="label" style="top:252px">Expiry Date</div>
  <div class="box box--pink" style="top:252px;left:184px"></div><div class="box box--pink" style="top:252px;left:198px"></div><span class="hint" style="top:252px;left:214px">MM</span>
  <div class="box box--pink" style="top:252px;left:232px"></div><div class="box box--pink" style="top:252px;left:246px"></div><span class="hint" style="top:252px;left:262px">YY</span>
  <div class="input input--pink" style="top:252px;left:280px;width:198px"></div>

  <div class="label" style="top:268px">CVV</div>
  <div class="box" style="top:268px;left:184px"></div><div class="box" style="top:268px;left:198px"></div><div class="box" style="top:268px;left:212px"></div>
  <div class="input" style="top:268px;left:230px;width:248px"></div>

  <div class="label" style="top:284px">Name as on the Credit Card</div>
  <div class="input input--pink" style="top:284px"></div>

  <div class="band" style="top:312px">I confirm that the payment is being made by me in respect of my policy for the amount of</div>
  <div class="aed" style="top:328px">AED</div>

  <div class="label" style="top:362px">Date</div>
  <div class="box box--pink" style="top:362px;left:184px"></div><div class="box box--pink" style="top:362px;left:198px"></div><span class="hint" style="top:362px;left:214px">DD</span>
  <div class="box box--pink" style="top:362px;left:232px"></div><div class="box box--pink" style="top:362px;left:246px"></div><span class="hint" style="top:362px;left:262px">MM</span>
  <div class="box box--pink" style="top:362px;left:280px"></div><div class="box box--pink" style="top:362px;left:294px"></div><span class="hint" style="top:362px;left:310px">YY</span>
  <div class="band" style="top:362px;left:330px;width:150px;height:10px"></div>

  <div class="band" style="top:384px">Cardholders Name &amp; Signature</div>
  <div class="panel" style="top:398px;height:12px"></div>
  <div class="band" style="top:414px;height:8px"></div>
  <div class="panel" style="top:424px;height:48px"></div>

  <div class="band band--notice" style="top:482px">Please note that by completing these payment details you are implicitly accepting the purchase of the<br>insurance policy for the amount specified above.</div>

  <footer class="page-footer">
    <svg class="footer-art" width="520" height="120" viewBox="0 0 520 120">
      <rect x="0" y="30" width="520" height="90" fill="#eef0f5"/>
      <polygon points="0,30 520,24 520,29 0,35" fill="#8b2a8f"/>
      <polygon points="330,88 520,88 520,96 322,96" fill="#8b2a8f"/>
      <polygon points="300,100 520,100 520,112 290,112" fill="#8b2a8f"/>
    </svg>
    <div class="legal">Registered name: Velmor Insurance Agency LLC<br>General Agents for Al Sahel National Insurance Co. (PSC)<br>Insurance Agents Registration No. 18<br>A member of the Velmor Insurance Group</div>
    <address class="office">
      <h3>Velmor Dubai</h3>
      Al Noor Street, Crescent Business Bldg.<br>
      <svg class="ic" viewBox="0 0 10 10"><path d="M5 0a4 4 0 0 1 4 4c0 3-4 6-4 6S1 7 1 4a4 4 0 0 1 4-4z" fill="#8b2a8f"/></svg>P.O.Box 4821, Dubai, UAE<br>
      <span class="pair"><span><svg class="ic" viewBox="0 0 10 10"><path d="M2 0l2 3-1 1c1 2 2 3 4 4l1-1 2 2-2 1C4 10 0 6 0 2z" fill="#8b2a8f"/></svg>+971 4 000 1234</span><span><svg class="ic" viewBox="0 0 10 10"><rect x="1" y="2" width="8" height="6" fill="#8b2a8f"/></svg>+971 4 000 5678</span></span><br>
      <span class="pair"><span><svg class="ic" viewBox="0 0 10 10"><circle cx="5" cy="5" r="4" fill="#8b2a8f"/></svg>www.velmorgulf-example.com</span><span><svg class="ic" viewBox="0 0 10 10"><rect x="0" y="2" width="10" height="6" fill="#8b2a8f"/></svg>info@velmorgulf-example.com</span></span>
    </address>
  </footer>
</section>

</body>
</html>
```